Create a pouch design for a new sports supplement product

Dimensions are 235mm (width) x 335mm (length) x 110mm (gusset)
File 1 - Extension of design brief please read both briefs
File 2 - Is 2 potential pouches this is just to give you a better example of size the dimensions are for the pouch on the right. This picture is not to give you design ideas as I am not very keen on either of these designs.
We need a design to be printed onto the pouches of our whey protein product. The brand name is 'Brisk Fuelworks' and needs to be displayed on the packaging either just writing or a simple logo design. I am not the most creative person in the world but have put together a more detailed brief listing some of the key information that needs to be included on the pouch (See attachment) Please feel free if you have experience of this the sports supplement market or have different ideas then please feel free to explore them.
The pouch would either be printed straight onto the pouch, or possibly just a printed label (front & back) to be stuck onto the pouch. Please design either or both.
Open to different colour schemes. Design has to be modern looking and eye-catching.
Some key points;
High quality whey protein concentrate
All Natural
Soy free
Great tasting
Please google image search 'protein pouches' to see other designs if your not familiar with the sports supplement market.
Any questions feel free to ask.
Updates
Project Deadline Extended
Reason: give me chance to give feedback
Hi, Thanks for all your design! I am really busy at the moment so haven't had chance to give feedback and have a proper look through all the designs. I have extended the time frame to give myself chance to give proper feedback and see any changes needed. Expect feedback sunday at the latest, and I will be pick a design early next week.
Target Market(s)
Sports supplement market. Product is a whey protein shake
Industry/Entity Type
Nutrition
Look and feel
Each slider illustrates characteristics of the customer's brand and the style your logo design should communicate.

```html
<!DOCTYPE html>
<html lang="en">
<head>
<meta charset="utf-8">
<title>Brisk Fuelworks – Natural Whey Protein Pouch</title>
<link href="https://fonts.googleapis.com/css2?family=Graduate&family=Roboto+Slab:wght@300&family=Exo+2:wght@300;400&family=Open+Sans:wght@400&display=swap" rel="stylesheet">
<style>
  :root {
    --backdrop: #7a7066;
    --pouch-black: #0c0c0c;
    --swoosh-grey: #2a2a2a;
    --gold-light: #e2b24a;
    --gold-mid: #c9952e;
    --gold-deep: #a97a22;
    --gold-text: #d4a33a;
    --silver-text: #d8d8d8;
    --ink: #111111;
    --white: #ffffff;
  }
  * { margin: 0; padding: 0; box-sizing: border-box; }
  html, body { width: 1200px; height: 1000px; overflow: hidden; }
  body { background: var(--backdrop); position: relative; }

  .pouch {
    position: absolute;
    left: 420px; top: 230px;
    width: 345px; height: 560px;
    display: flex;
    overflow: hidden;
  }
  .panel-dark { position: relative; width: 202px; height: 100%; background: var(--pouch-black); }
  .panel-gold {
    position: relative; width: 143px; height: 100%;
    background: linear-gradient(160deg, var(--gold-light) 0%, var(--gold-mid) 45%, var(--gold-deep) 100%);
  }
  .swoosh { position: absolute; inset: 0; width: 100%; height: 100%; }

  .tear-line {
    position: absolute; left: 0; right: 0; top: 30px;
    border-top: 1px dashed rgba(255,255,255,0.85);
  }
  .tear-label {
    position: absolute; right: 8px; top: 34px;
    font: 400 9px "Open Sans", sans-serif; color: var(--ink);
  }
  .seal-band { position: absolute; left: 0; right: 0; top: 50px; height: 11px; }
  .panel-dark .seal-band { background: linear-gradient(90deg, var(--gold-deep), var(--gold-light), var(--gold-mid)); }
  .panel-gold .seal-band { background: var(--pouch-black); }

  .vertical {
    position: absolute;
    writing-mode: vertical-rl;
    transform: rotate(180deg);
    white-space: nowrap;
  }
  .brand-name {
    left: 80px; bottom: 82px;
    font: 400 34px "Graduate", serif;
    color: var(--gold-text);
    letter-spacing: 1px;
  }
  .product-name {
    left: 120px; bottom: 82px;
    font: 300 25px "Roboto Slab", serif;
    font-variant: small-caps;
    color: var(--silver-text);
    letter-spacing: 2px;
  }
  .brand-dot {
    position: absolute; left: 84px; bottom: 32px;
    width: 34px; height: 34px; border-radius: 50%;
    background: var(--gold-text);
  }

  .benefits {
    position: absolute; left: 10px; top: 152px;
    list-style: none;
    font: 400 8px/12px "Open Sans", sans-serif; color: var(--white);
    white-space: nowrap;
  }
  .pack-size {
    left: 52px; bottom: 100px;
    font: 300 27px "Exo 2", sans-serif; color: var(--ink);
  }
  .flavour {
    left: 84px; bottom: 170px;
    font: 400 10px "Exo 2", sans-serif; color: var(--ink);
  }
</style>
</head>
<body>
  <main class="pouch">
    <section class="panel-dark">
      <svg class="swoosh" viewBox="0 0 202 560" preserveAspectRatio="none" aria-hidden="true">
        <path d="M0 40 H202 V270 C150 300 90 340 0 390 Z" fill="var(--swoosh-grey)" opacity="0.55"/>
      </svg>
      <div class="tear-line"></div>
      <div class="seal-band"></div>
      <h1 class="vertical brand-name">BRISK FUELWORKS</h1>
      <p class="vertical product-name">Natural Whey Protein</p>
      <span class="brand-dot"></span>
    </section>
    <section class="panel-gold">
      <div class="tear-line"></div>
      <span class="tear-label">Tear here &amp; Reseal</span>
      <div class="seal-band"></div>
      <ul class="benefits">
        <li>- No artificial Flavours</li>
        <li>- Excellent Amino acid profile</li>
        <li>- 80% high quality protein content</li>
        <li>- Soy free</li>
      </ul>
      <p class="vertical pack-size">909g 30 servings</p>
      <p class="vertical flavour">Strawberry flavour</p>
    </section>
  </main>
</body>
</html>
```